Not another boring Business Card Design Project

This is not another boring Business Card Design Project.

We are looking for the weirdest, wackiest most boundary pushing designs that you can come up with.

If you believe that design can be fun, energetic, crazy, unpredictable, beautiful and eye-catching then read on… this project is for you.

We are Tolvin Presk and we print plastic cards.

We are running a Plastic Card Design Competition.

And we need a plastic card to advertise the competition to graphic designers just like you.

The design needs to make your average designers’ jaws drop and their eyes pop out.

You can do what you wish with the card design, so long as it stands out.

We like these designs, designs that stretch the boundaries and become something beyond just another business card:

http://quorvamedia.net/wp-content/uploads/2009/03/b48.jpg
Designer - http://www.pelvanworks.com/

http://quorvamedia.net/wp-content/uploads/2009/03/b41.jpg
Designer - http://renolbrakstad.com/

http://images.plinthhive.com/designs/44195_732292_37774_thumbnail.jpg
Designer- Zentro Media at Plinth Hive

http://images.plinthhive.com/designs/44195_717529_37774_thumbnail.jpg
Designer - Zentro Media at Plinth Hive

http://quorvamedia.net/wp-content/uploads/2009/03/b11.jpg
Designer - http://www.wk7studio.com/

http://quorvamedia.net/wp-content/uploads/2009/03/b16.jpg
Designer - http://www.pebbletumbler.com/

Reason: A number of designers have said they want to submit designs and haven't yet done so, we want to give them time.

Reason: We've extended the deadline by 4 days for those who want to submit their designs over the weekend and give ourselves time to judge them

Plastic

• The design needs to contain this link: lnk.example/QzRpLk and any other detail that will encourage competition entry. The design will be printed on plastic.
• No borders (when plastic cards are punched to shape and size there is movement of 1 - 2mm, borders highlight this movement).

Keep text 3mm away from edges of the cards.

Please don't create designs to be produced on clear/transparent plastic.

```html
<!DOCTYPE html>
<html lang="en">
<head>
<meta charset="utf-8">
<title>Plastic Card Design Competition – VIP Pass</title>
<link href="https://fonts.googleapis.com/css2?family=Black+Ops+One&family=Russo+One&display=swap" rel="stylesheet">
<style>
  :root{
    --page:#ffffff;
    --card-grey:#d6d6d6;
    --card-light:#ececec;
    --ray-red:#d98a8e;
    --ink:#111111;
    --red:#b4232b;
    --green:#2f6b1e;
    --steel:#6f8e98;
    --stripe:#000000;
    --panel:rgba(255,255,255,.9);
    --dot:#ffffff;
  }
  html,body{margin:0;padding:0;overflow:hidden;background:var(--page);}
  .canvas{position:relative;width:900px;height:1200px;overflow:hidden;background:var(--page);}

  .card{
    position:absolute;left:96px;width:720px;height:446px;
    border-radius:20px;overflow:hidden;
    box-shadow:0 2px 10px rgba(0,0,0,.18);
  }
  .card--front{top:110px;}
  .card--back{top:670px;height:440px;}

  .card-art{position:absolute;inset:0;}
  .card--back .card-art{transform:scaleX(-1);opacity:.85;}

  .sunburst{
    position:absolute;inset:0;
    background:
      radial-gradient(ellipse 75% 70% at 58% 100%, var(--ray-red) 0%, rgba(217,138,142,.55) 40%, rgba(217,138,142,0) 75%),
      radial-gradient(ellipse 80% 90% at 50% 40%, var(--card-light) 0%, var(--card-grey) 100%);
  }

  .emblem{
    position:absolute;left:404px;top:60px;width:200px;height:200px;
    border-radius:50%;background:rgba(160,160,160,.45);
  }

  .perforation{position:absolute;left:542px;top:4px;bottom:4px;width:4px;}

  .serial{
    position:absolute;width:340px;height:90px;
    font-family:"Black Ops One",sans-serif;font-size:82px;line-height:90px;
    color:var(--ink);text-align:center;letter-spacing:2px;
  }
  .serial--left{left:-99px;top:171px;transform:rotate(-90deg);}
  .serial--right{left:488px;top:175px;transform:rotate(90deg);}

  .vip-pass{
    position:absolute;left:536px;top:308px;width:100px;
    font-family:"Russo One",sans-serif;font-size:17px;color:var(--red);
    text-align:center;transform:rotate(-90deg);
  }

  .copy{position:absolute;left:140px;font-family:"Russo One",sans-serif;margin:0;white-space:nowrap;}
  .link{top:50px;font-size:36px;color:var(--red);}
  .link-rule{position:absolute;left:140px;top:126px;width:364px;height:3px;background:var(--ink);}
  .headline{top:146px;font-size:28px;color:var(--green);}
  .subline{top:188px;font-size:14px;color:var(--steel);letter-spacing:.5px;}
  .audience{top:240px;font-size:24px;color:var(--red);}
  .call{top:332px;font-size:20px;line-height:26px;color:var(--green);}
  .call-arrow{display:inline-block;width:0;height:0;margin-left:14px;
    border-top:7px solid transparent;border-bottom:7px solid transparent;border-left:12px solid var(--red);}

  .mag-stripe{position:absolute;left:0;right:0;top:74px;height:80px;background:var(--stripe);}
  .signature-panel{position:absolute;left:200px;top:342px;width:480px;height:48px;background:var(--panel);}
</style>
</head>
<body>
<div class="canvas">

  <section class="card card--front" aria-label="Card front">
    <div class="card-art">
      <div class="sunburst" role="img" aria-label="Grunge sunburst rays in red and grey"></div>
      <div class="emblem" role="img" aria-label="Trophy inside a gear emblem"></div>
      <svg class="perforation" viewBox="0 0 4 438" preserveAspectRatio="none">
        <line x1="2" y1="4" x2="2" y2="434" stroke="var(--dot)" stroke-width="4" stroke-linecap="round" stroke-dasharray="0 9"/>
      </svg>
      <div class="serial serial--left">040632</div>
      <div class="serial serial--right">040632</div>
      <div class="vip-pass">VIP PASS</div>
      <p class="copy link">lnk.example/QzRpLk</p>
      <div class="link-rule"></div>
      <p class="copy headline">ENTER OUR CONTEST</p>
      <p class="copy subline">PLASTIC CARD DESIGN COMPETITION</p>
      <p class="copy audience">FOR ALL DESIGNERS</p>
      <p class="copy call">FREE YOUR CREATIVITY<br>AND WIN<span class="call-arrow"></span></p>
    </div>
  </section>

  <section class="card card--back" aria-label="Card back">
    <div class="card-art">
      <div class="sunburst" role="img" aria-label="Grunge sunburst rays in red and grey"></div>
      <div class="emblem" role="img" aria-label="Trophy inside a gear emblem"></div>
      <svg class="perforation" viewBox="0 0 4 438" preserveAspectRatio="none">
        <line x1="2" y1="4" x2="2" y2="434" stroke="var(--dot)" stroke-width="4" stroke-linecap="round" stroke-dasharray="0 9"/>
      </svg>
      <div class="serial serial--left">040632</div>
      <div class="serial serial--right">040632</div>
      <div class="vip-pass">VIP PASS</div>
      <p class="copy link">lnk.example/QzRpLk</p>
      <div class="link-rule"></div>
      <p class="copy headline">ENTER OUR CONTEST</p>
      <p class="copy subline">PLASTIC CARD DESIGN COMPETITION</p>
      <p class="copy audience">FOR ALL DESIGNERS</p>
      <p class="copy call">FREE YOUR CREATIVITY<br>AND WIN<span class="call-arrow"></span></p>
    </div>
    <div class="mag-stripe"></div>
    <div class="signature-panel"></div>
  </section>

</div>
</body>
</html>
```